Lumen Harbor Business Card Design Project

We have recently rebranded and would like to design new business cards that incorporate the corporate logo - double sided cards with corporate logo on one side and contact details on the other

Target Market(s)

Sophisticated and high net worth investors and finance industry professionals

Industry/Entity Type

Funds Management

Contact Information for Business Card

The card should prominently feature the company name and logo. Other details will be standard contact details for each staff member - name, address, phone, email, website

Colors
0054AA
0677BA
7BADD7
CADEEF
E8F1F8

Requirements
Must have
• Double-sided design with one side prominently featuring the corporate logo and the other side with all standard contact details

```html
<!DOCTYPE html>
<html lang="en">
<head>
<meta charset="UTF-8">
<title>Lumen Harbor – Business Card</title>
<link href="https://fonts.googleapis.com/css2?family=Cinzel:wght@500;600&family=Lato:wght@400&display=swap" rel="stylesheet">
<style>
  :root {
    --stage: #737373;
    --navy: #214572;
    --paper: #ffffff;
  }
  * { margin: 0; padding: 0; box-sizing: border-box; }
  html, body {
    width: 1200px;
    height: 1200px;
    overflow: hidden;
    background: var(--stage);
  }
  .card {
    position: absolute;
    left: 281px;
    width: 638px;
    height: 365px;
    border-radius: 26px;
    overflow: hidden;
  }
  .card--front { top: 195px; background: var(--navy); color: var(--paper); }
  .card--back { top: 639px; background: var(--paper); }

  .person {
    position: absolute;
    left: 46px;
    top: 116px;
  }
  .person__name {
    font-family: "Cinzel", serif;
    font-weight: 500;
    font-size: 29px;
    letter-spacing: 0.5px;
    line-height: 1.1;
  }
  .person__role {
    font-family: "Lato", sans-serif;
    font-size: 16px;
    margin-top: 2px;
  }

  .contact {
    position: absolute;
    left: 46px;
    top: 193px;
    list-style: none;
    font-family: "Lato", sans-serif;
    font-size: 14.5px;
    letter-spacing: 0.6px;
  }
  .contact__item {
    display: flex;
    align-items: flex-start;
    line-height: 19px;
    margin-bottom: 3px;
  }
  .contact__item:last-child { margin-top: 2px; }
  .contact__icon {
    width: 11px;
    height: 11px;
    margin: 4px 13px 0 0;
    fill: var(--paper);
    flex: none;
  }

  .wordmark {
    position: absolute;
    left: 0;
    right: 0;
    top: 196px;
    text-align: center;
    font-family: "Cinzel", serif;
    font-weight: 600;
    font-size: 48px;
    letter-spacing: 1px;
    color: var(--navy);
  }
</style>
</head>
<body>
  <section class="card card--front">
    <div class="person">
      <h1 class="person__name">Daniel Reeve</h1>
      <p class="person__role">Founder &amp; CEO</p>
    </div>
    <ul class="contact">
      <li class="contact__item">
        <svg class="contact__icon" viewBox="0 0 12 12"><path d="M2.5 0.5l2 2.5-1.2 1.3c.7 1.6 2 2.9 3.5 3.6L8 6.7l2.6 2-1.2 2.3C5 10.6 1.2 6.8 .6 2.3z"/></svg>
        <span>(555) 214-3870</span>
      </li>
      <li class="contact__item">
        <svg class="contact__icon" viewBox="0 0 12 12"><path d="M3 0h6v12H3zM4.2 1.2v8h3.6v-8zM5.4 10h1.2v1H5.4z" fill-rule="evenodd"/></svg>
        <span>(555) 214-3870</span>
      </li>
      <li class="contact__item">
        <svg class="contact__icon" viewBox="0 0 12 12"><path d="M0 2.5h12v1L6 7 0 3.5zM0 4.8l6 3.5 6-3.5V10H0z"/></svg>
        <span>info@lumenharbor.com</span>
      </li>
      <li class="contact__item">
        <svg class="contact__icon" viewBox="0 0 12 12"><circle cx="6" cy="6" r="5.5"/><path d="M3 3.5c1 .3 1.5 1 1.2 2 .8.3 1 1.3.5 2.2M7.5 1.3c-.2 1 .4 1.7 1.5 1.7.3 1 1.3 1.3 2.2 1" stroke="#214572" stroke-width="1" fill="none"/></svg>
        <span>lumenharbor.com</span>
      </li>
      <li class="contact__item">
        <svg class="contact__icon" viewBox="0 0 12 12"><path d="M6 0a4 4 0 0 1 4 4c0 3-4 8-4 8S2 7 2 4a4 4 0 0 1 4-4zm0 2.4a1.6 1.6 0 1 0 0 3.2 1.6 1.6 0 0 0 0-3.2z" fill-rule="evenodd"/></svg>
        <span>418 Lantern Way<br>Fairview, CT 06400</span>
      </li>
    </ul>
  </section>

  <section class="card card--back">
    <p class="wordmark">Lumen Harbor</p>
  </section>
</body>
</html>
```